Werbebanner für Textilreinigung
Zielgruppe
Wir sind eine Textilreinigung mit einem großen Spektrum an Leistungen.
Unsere Zielgruppe sind Privat Personen die ihre Textilien zum reinigen zu uns bringen.
Aufgabenstellung
Es sollen 5 Straßenbanner designt werden. Diese werden bei Ortseinfahrten/- ausfahrten, aufgehängt. Das Design soll modern sein und zu unserem Logo passen. Die Herausforderung bei den Straßenbannern ist die Zielgruppe, die Autofahrer. Der Banner wird beim Vorbeifahren für nur 1-2 Sekunden gesehen. Auf jedem Banner soll ein Sonderangebot mit eingebaut werden. Zu der Zeit in der der Banner aufgehängt ist, erhält der Kunde 20% auf die jeweilige Dienstleistung.
Hier die verschiedenen Banner:
-Betten & Daunenreinigung | -Trachten und Lederreinigung | -Braut & Festtagskleider reinigung |-Teppichwäsche (inkl. kostenlosen Abhol und Lieferservice) |-Hemdenservice
Bannergröße beträgt 100cm(H) x 300cm(B)
Das gilt für alle 5 verschiedenen Banner.
Es soll auf jedem Banner stehen:
-Sonderangebot 20%
-unser Logo (siehe Dateien)
-unsere Adresse
-Telefonnummer
-Aufruf zur Aktion
Anmerkung: Auf der EPS.Datei muss ein kleiner Schriftzug hinzugefügt werden der auf der PDF. zu sehen ist.

```html
<!DOCTYPE html>
<html lang="de">
<head>
<meta charset="utf-8">
<title>Straßenbanner Textilreinigung</title>
<link href="https://fonts.googleapis.com/css2?family=Roboto+Condensed:wght@400;700;900&display=swap" rel="stylesheet">
<style>
  :root{
    --red:#b5121b;
    --blue:#2b3990;
    --green:#7cbf3a;
    --white:#ffffff;
    --pearl:#e4e4e8;
  }
  *{margin:0;padding:0;box-sizing:border-box}
  html,body{width:1200px;height:2400px;overflow:hidden}
  body{
    background:linear-gradient(180deg,#cfcfcf 0%,#dedede 50%,#cdcdcd 100%);
    font-family:"Roboto Condensed",Arial,sans-serif;
    position:relative;
  }
  .banner{
    position:absolute;left:103px;width:994px;height:331px;
    background:var(--white);overflow:hidden;
    box-shadow:0 2px 6px rgba(0,0,0,.15);
  }
  .banner svg.shapes{position:absolute;inset:0;width:100%;height:100%}
  .service-bar{
    position:absolute;right:0;top:17px;height:70px;
    background:var(--red);color:var(--white);
    font-weight:900;font-size:46px;line-height:70px;
    padding:0 34px 0 20px;white-space:nowrap;letter-spacing:-.3px;
  }
  .service-bar.tall{height:96px;line-height:1}
  .service-bar.tall .main{display:block;text-align:right;padding-top:8px;font-size:48px}
  .service-bar.tall .sub{display:block;text-align:right;font-size:21px;font-weight:700;padding-top:4px}
  .offer{
    position:absolute;left:422px;top:100px;width:190px;
    text-align:center;color:var(--red);font-weight:900;line-height:1;
    transform:rotate(3deg);
  }
  .offer .now{font-size:27px;display:block}
  .offer .percent{font-size:78px;display:block;letter-spacing:-2px;margin-top:-2px}
  .offer .save{font-size:46px;display:block;margin-top:-4px}
  .brand-mark{
    position:absolute;left:648px;top:128px;width:52px;height:52px;border-radius:50%;
    background:var(--pearl);
  }
  .brand{position:absolute;left:731px;top:126px;width:229px;color:var(--blue);line-height:1;white-space:nowrap}
  .brand .tagline{display:block;font-size:15px;font-weight:400;letter-spacing:.3px;line-height:19px}
  .brand .name{display:block;font-size:44px;font-weight:700;margin-top:4px;letter-spacing:0}
  .brand .web{display:block;font-size:29px;font-weight:700;margin-top:8px}
  .contact{
    position:absolute;right:34px;top:262px;height:69px;
    display:flex;align-items:center;gap:8px;color:var(--white);
    font-weight:700;white-space:nowrap;
  }
  .contact .town{font-size:27px}
  .contact .street{font-size:40px}
  .contact .phone{font-size:27px;display:flex;align-items:center;gap:5px}
  .contact .dot{font-size:27px}
  .contact svg{width:22px;height:22px}
</style>
</head>
<body>

<section class="banner" style="top:167px">
  <svg class="shapes" viewBox="0 0 828 276" preserveAspectRatio="none">
    <defs><linearGradient id="ph1" x1="0" y1="0" x2="1" y2="1"><stop offset="0" stop-color="#ece9e6"/><stop offset=".6" stop-color="#c9a99a"/><stop offset="1" stop-color="#7a3a34"/></linearGradient></defs>
    <rect x="0" y="218" width="828" height="58" fill="var(--blue)"/>
    <path role="img" aria-label="Foto: Paar in Dirndl und Lederhose" d="M0 0H378C372 80 320 210 160 276H0Z" fill="url(#ph1)"/>
    <path d="M378 0C372 80 320 210 160 276" fill="none" stroke="var(--green)" stroke-width="7"/>
  </svg>
  <div class="service-bar" style="left:356px">Trachten- &amp; Lederreinigung</div>
  <div class="offer"><span class="now">JETZT</span><span class="percent">20%</span><span class="save">SPAREN!</span></div>
  <div class="brand-mark"></div>
  <div class="brand"><span class="tagline">ZENTRALREINIGUNG<br>GROSSWÄSCHEREI</span><span class="name">GLANZWERK</span><span class="web">www.glanzwerk.net</span></div>
  <div class="contact"><span class="town">LINDACH</span><span class="dot">•</span><span class="street">BIRKENWEG 12</span><span class="dot">•</span><span class="phone"><svg viewBox="0 0 24 24"><path fill="#fff" d="M6.6 10.8a15 15 0 0 0 6.6 6.6l2.2-2.2c.3-.3.7-.4 1-.2 1.1.4 2.3.6 3.6.6.6 0 1 .4 1 1V20c0 .6-.4 1-1 1A17 17 0 0 1 3 4c0-.6.4-1 1-1h3.5c.6 0 1 .4 1 1 0 1.3.2 2.5.6 3.6.1.3 0 .7-.2 1z"/></svg>08123 - 4567</span></div>
</section>

<section class="banner" style="top:602px">
  <svg class="shapes" viewBox="0 0 828 276" preserveAspectRatio="none">
    <defs><linearGradient id="ph2" x1="0" y1="0" x2="0" y2="1"><stop offset="0" stop-color="#9aa0a0"/><stop offset=".5" stop-color="#b8b2aa"/><stop offset="1" stop-color="#6e9a45"/></linearGradient></defs>
    <rect x="0" y="218" width="828" height="58" fill="var(--blue)"/>
    <path role="img" aria-label="Foto: Brautpaar mit Hochzeitsgästen auf einer Wiese" d="M0 0H378C372 80 320 210 160 276H0Z" fill="url(#ph2)"/>
    <path d="M378 0C372 80 320 210 160 276" fill="none" stroke="var(--green)" stroke-width="7"/>
  </svg>
  <div class="service-bar" style="left:306px">Braut- &amp; Festtagskleiderreinigung</div>
  <div class="offer"><span class="now">JETZT</span><span class="percent">20%</span><span class="save">SPAREN!</span></div>
  <div class="brand-mark"></div>
  <div class="brand"><span class="tagline">ZENTRALREINIGUNG<br>GROSSWÄSCHEREI</span><span class="name">GLANZWERK</span><span class="web">www.glanzwerk.net</span></div>
  <div class="contact"><span class="town">LINDACH</span><span class="dot">•</span><span class="street">BIRKENWEG 12</span><span class="dot">•</span><span class="phone"><svg viewBox="0 0 24 24"><path fill="#fff" d="M6.6 10.8a15 15 0 0 0 6.6 6.6l2.2-2.2c.3-.3.7-.4 1-.2 1.1.4 2.3.6 3.6.6.6 0 1 .4 1 1V20c0 .6-.4 1-1 1A17 17 0 0 1 3 4c0-.6.4-1 1-1h3.5c.6 0 1 .4 1 1 0 1.3.2 2.5.6 3.6.1.3 0 .7-.2 1z"/></svg>08123 - 4567</span></div>
</section>

<section class="banner" style="top:1038px">
  <svg class="shapes" viewBox="0 0 828 276" preserveAspectRatio="none">
    <defs><linearGradient id="ph3" x1="0" y1="0" x2="1" y2="1"><stop offset="0" stop-color="#cdb6a4"/><stop offset=".5" stop-color="#eeeae6"/><stop offset="1" stop-color="#f7f5f3"/></linearGradient></defs>
    <rect x="0" y="218" width="828" height="58" fill="var(--blue)"/>
    <path role="img" aria-label="Foto: schlafende Frau in weißer Bettwäsche" d="M0 0H378C372 80 320 210 160 276H0Z" fill="url(#ph3)"/>
    <path d="M378 0C372 80 320 210 160 276" fill="none" stroke="var(--green)" stroke-width="7"/>
  </svg>
  <div class="service-bar" style="left:359px">Betten- &amp; Daunenreinigung</div>
  <div class="offer"><span class="now">JETZT</span><span class="percent">20%</span><span class="save">SPAREN!</span></div>
  <div class="brand-mark"></div>
  <div class="brand"><span class="tagline">ZENTRALREINIGUNG<br>GROSSWÄSCHEREI</span><span class="name">GLANZWERK</span><span class="web">www.glanzwerk.net</span></div>
  <div class="contact"><span class="town">LINDACH</span><span class="dot">•</span><span class="street">BIRKENWEG 12</span><span class="dot">•</span><span class="phone"><svg viewBox="0 0 24 24"><path fill="#fff" d="M6.6 10.8a15 15 0 0 0 6.6 6.6l2.2-2.2c.3-.3.7-.4 1-.2 1.1.4 2.3.6 3.6.6.6 0 1 .4 1 1V20c0 .6-.4 1-1 1A17 17 0 0 1 3 4c0-.6.4-1 1-1h3.5c.6 0 1 .4 1 1 0 1.3.2 2.5.6 3.6.1.3 0 .7-.2 1z"/></svg>08123 - 4567</span></div>
</section>

<section class="banner" style="top:1474px">
  <svg class="shapes" viewBox="0 0 828 276" preserveAspectRatio="none">
    <defs><linearGradient id="ph4" x1="0" y1="0" x2="1" y2="0"><stop offset="0" stop-color="#8aa6c8"/><stop offset=".45" stop-color="#e9ddd6"/><stop offset="1" stop-color="#c65a5a"/></linearGradient></defs>
    <rect x="0" y="218" width="828" height="58" fill="var(--blue)"/>
    <path role="img" aria-label="Foto: junge Frau mit Hemden vor einer Kleiderstange" d="M0 0H378C372 80 320 210 160 276H0Z" fill="url(#ph4)"/>
    <path d="M378 0C372 80 320 210 160 276" fill="none" stroke="var(--green)" stroke-width="7"/>
  </svg>
  <div class="service-bar" style="left:572px">Hemdenservice</div>
  <div class="offer"><span class="now">JETZT</span><span class="percent">20%</span><span class="save">SPAREN!</span></div>
  <div class="brand-mark"></div>
  <div class="brand"><span class="tagline">ZENTRALREINIGUNG<br>GROSSWÄSCHEREI</span><span class="name">GLANZWERK</span><span class="web">www.glanzwerk.net</span></div>
  <div class="contact"><span class="town">LINDACH</span><span class="dot">•</span><span class="street">BIRKENWEG 12</span><span class="dot">•</span><span class="phone"><svg viewBox="0 0 24 24"><path fill="#fff" d="M6.6 10.8a15 15 0 0 0 6.6 6.6l2.2-2.2c.3-.3.7-.4 1-.2 1.1.4 2.3.6 3.6.6.6 0 1 .4 1 1V20c0 .6-.4 1-1 1A17 17 0 0 1 3 4c0-.6.4-1 1-1h3.5c.6 0 1 .4 1 1 0 1.3.2 2.5.6 3.6.1.3 0 .7-.2 1z"/></svg>08123 - 4567</span></div>
</section>

<section class="banner" style="top:1909px">
  <svg class="shapes" viewBox="0 0 828 276" preserveAspectRatio="none">
    <defs><linearGradient id="ph5" x1="0" y1="0" x2="1" y2="1"><stop offset="0" stop-color="#8f8f8f"/><stop offset=".5" stop-color="#b9aea8"/><stop offset="1" stop-color="#a6a6a6"/></linearGradient></defs>
    <rect x="0" y="218" width="828" height="58" fill="var(--blue)"/>
    <path role="img" aria-label="Foto: Frau liegt entspannt auf einem grauen Hochflorteppich" d="M0 0H378C372 80 320 210 160 276H0Z" fill="url(#ph5)"/>
    <path d="M378 0C372 80 320 210 160 276" fill="none" stroke="var(--green)" stroke-width="7"/>
  </svg>
  <div class="service-bar tall" style="left:544px"><span class="main">Teppichwäsche</span><span class="sub">(inkl. kostenlosen Abhol und Lieferservice)</span></div>
  <div class="offer" style="top:108px;transform:rotate(2deg) scale(.93)"><span class="now">JETZT</span><span class="percent">20%</span><span class="save">SPAREN!</span></div>
  <div class="brand-mark"></div>
  <div class="brand"><span class="tagline">ZENTRALREINIGUNG<br>GROSSWÄSCHEREI</span><span class="name">GLANZWERK</span><span class="web">www.glanzwerk.net</span></div>
  <div class="contact"><span class="town">LINDACH</span><span class="dot">•</span><span class="street">BIRKENWEG 12</span><span class="dot">•</span><span class="phone"><svg viewBox="0 0 24 24"><path fill="#fff" d="M6.6 10.8a15 15 0 0 0 6.6 6.6l2.2-2.2c.3-.3.7-.4 1-.2 1.1.4 2.3.6 3.6.6.6 0 1 .4 1 1V20c0 .6-.4 1-1 1A17 17 0 0 1 3 4c0-.6.4-1 1-1h3.5c.6 0 1 .4 1 1 0 1.3.2 2.5.6 3.6.1.3 0 .7-.2 1z"/></svg>08123 - 4567</span></div>
</section>

</body>
</html>
```